Business Card Design Project

I am an aviation professional (corporate pilot), and am looking to market myself to the business jet operators for short term crew leasing. The card should have name and contact info on the front side; qualifications, licenses held and type ratings on the back side.
Company name is: Harbinvale Skyline Partners Inc.
Updates

Sorry for the delay. will reply in another day or two.
best regards,

P

Target Market(s)

Business Jet Management companies and private jet operators

Industry/Entity Type

Business

Requirements
Must have
• It needs to be an aviation inspired design.

```html
<!DOCTYPE html>
<html lang="en">
<head>
<meta charset="utf-8">
<title>Harbinvale Skyline Partners Inc. – Business Card</title>
<link rel="stylesheet" href="https://fonts.googleapis.com/css2?family=Cinzel:wght@700&family=Nunito:ital,wght@1,800&family=Roboto:wght@500&display=swap">
<style>
  :root {
    --backdrop: #000000;
    --card: #ffffff;
    --brand-red: #c7000b;
    --sand: #b9a594;
    --steel: #7a7a7a;
    --ink: #111111;
    --figure-shade: #1a1a1a;
  }
  html, body {
    margin: 0;
    padding: 0;
    width: 1200px;
    height: 1200px;
    overflow: hidden;
    background: var(--backdrop);
  }
  .business-card {
    position: absolute;
    left: 100px;
    top: 276px;
    width: 1014px;
    height: 567px;
    background: var(--card);
    overflow: hidden;
  }
  .brand-stripes {
    position: absolute;
    left: 0;
    top: 0;
    width: 1014px;
    height: 567px;
  }
  .brand-mark {
    position: absolute;
    left: 30px;
    top: 90px;
    display: flex;
    align-items: center;
    gap: 10px;
    font-family: "Cinzel", serif;
    font-weight: 700;
    font-size: 22px;
    color: var(--brand-red);
    letter-spacing: 1px;
  }
  .brand-mark__square {
    width: 18px;
    height: 18px;
    background: var(--brand-red);
  }
  .company-name {
    position: absolute;
    right: 24px;
    top: 14px;
    margin: 0;
    font-family: "Cinzel", serif;
    font-weight: 700;
    font-size: 29px;
    color: var(--steel);
    letter-spacing: 0.5px;
    white-space: nowrap;
  }
  .person-name {
    position: absolute;
    left: 519px;
    top: 44px;
    margin: 0;
    font-family: "Nunito", sans-serif;
    font-style: italic;
    font-weight: 800;
    font-size: 40px;
    line-height: 1;
    color: var(--brand-red);
    letter-spacing: 1px;
  }
  .person-title {
    position: absolute;
    left: 518px;
    top: 87px;
    margin: 0;
    font-family: "Roboto", sans-serif;
    font-weight: 500;
    font-size: 18px;
    color: var(--ink);
    letter-spacing: 0.6px;
  }
  .crew-figures {
    position: absolute;
    left: 91px;
    top: 231px;
    width: 374px;
    height: 270px;
    background: linear-gradient(180deg, #2a2a2a 0%, var(--figure-shade) 100%);
    opacity: 0.92;
  }
  .credentials-link {
    position: absolute;
    left: 669px;
    top: 528px;
    display: flex;
    align-items: center;
    gap: 8px;
    font-family: "Roboto", sans-serif;
    font-weight: 500;
    font-size: 14px;
    color: var(--brand-red);
    letter-spacing: 0.3px;
  }
  .credentials-link svg {
    display: block;
  }
</style>
</head>
<body>
  <div class="business-card">
    <svg class="brand-stripes" viewBox="0 0 1014 567" aria-hidden="true">
      <rect x="0" y="366" width="1014" height="37" fill="var(--brand-red)"/>
      <rect x="0" y="408" width="1014" height="36" fill="var(--brand-red)"/>
      <rect x="0" y="444" width="1014" height="57" fill="var(--sand)"/>
      <polygon points="754,366 890,366 752,501 616,501" fill="var(--card)"/>
    </svg>

    <div class="brand-mark">
      <span class="brand-mark__square"></span>
      <span>Harbinvale</span>
    </div>

    <h1 class="company-name">HARBINVALE SKYLINE PARTNERS, INC.</h1>
    <h2 class="person-name">Dana Rowell</h2>
    <p class="person-title">AVIATION PROFESSIONAL</p>

    <div class="crew-figures" role="img" aria-label="Dark silhouettes of four standing aviation crew members in business attire"></div>

    <div class="credentials-link">
      <span>CREDENTIALS</span>
      <svg width="218" height="12" viewBox="0 0 218 12" aria-hidden="true">
        <line x1="0" y1="6" x2="204" y2="6" stroke="var(--ink)" stroke-width="1.6"/>
        <polygon points="218,6 196,1 200,6 196,11" fill="var(--ink)"/>
      </svg>
    </div>
  </div>
</body>
</html>
```